A property investment company, looking to provide lovely sustainable homes for familys and individua

For a small investment business i am starting which will buy and refurbish unloved houses and apartments to rent out or resell. the company name is my family surname (HARGREAVE). <br/>i would like the design to be simple with maybe some emphasis on an ethical and sustainable/environmentally friendly approach with a branding of maybe trees blended with some houses and or apartments.<br/>The colours i like for this design would be mainly green on either a white or black background.
Target Market(s)
This business card is to be used for professional people such as estate agents
mortgage brokers, solicitors and trades people.
Industry/Entity Type
Real Estate
Contact Information for Business Card
owner/director-Martin hargreave
e-mail-martin@hvholdings.co.uk
website-hargreavehomeholdings.co.uk
mobile-07700945318
landline-02079460581
Look and feel

```html
<!DOCTYPE html>
<html lang="en">
<head>
<meta charset="UTF-8">
<title>Martin Hargreave – Business Card</title>
<link href="https://fonts.googleapis.com/css2?family=Inter:wght@200;300;700&display=swap" rel="stylesheet">
<style>
  :root {
    --backdrop: #ecebe8;
    --card: #ffffff;
    --green: #6aa444;
    --green-deep: #4e8a2c;
    --green-text: #6f9a58;
    --tree-tint: #eaf4ea;
    --white: #ffffff;
  }
  * { margin: 0; padding: 0; box-sizing: border-box; }
  html, body {
    width: 1200px;
    height: 900px;
    overflow: hidden;
    background: var(--backdrop);
  }
  .business-card {
    position: absolute;
    left: 100px;
    top: 172px;
    width: 1000px;
    height: 556px;
    background: var(--card);
    overflow: hidden;
    box-shadow: 0 6px 24px rgba(0, 0, 0, 0.12);
    font-family: 'Inter', sans-serif;
  }
  .tree-artwork {
    position: absolute;
    left: 395px;
    top: 75px;
    width: 540px;
    height: 440px;
    border-radius: 48% 48% 20% 20%;
    background: radial-gradient(ellipse at 55% 40%, var(--tree-tint) 0%, rgba(234, 244, 234, 0.6) 55%, rgba(255, 255, 255, 0) 78%);
  }
  .identity {
    position: absolute;
    left: 56px;
    top: 52px;
  }
  .identity-name {
    font-weight: 700;
    font-size: 43px;
    line-height: 1.1;
    color: var(--green-deep);
    letter-spacing: -0.3px;
  }
  .identity-role {
    font-weight: 300;
    font-size: 42px;
    line-height: 1.15;
    color: var(--green);
  }
  .contact-list {
    position: absolute;
    right: 56px;
    top: 222px;
    list-style: none;
    text-align: right;
  }
  .contact-item {
    font-weight: 200;
    font-size: 38px;
    line-height: 48px;
    color: var(--green-text);
    letter-spacing: 0.3px;
  }
  .ground-band {
    position: absolute;
    left: 0;
    bottom: 0;
    width: 1000px;
    height: 130px;
  }
  .brand-name {
    position: absolute;
    right: 26px;
    bottom: 20px;
    font-weight: 700;
    font-size: 16px;
    letter-spacing: 1px;
    color: var(--white);
  }
</style>
</head>
<body>
  <article class="business-card">
    <div class="tree-artwork" role="img" aria-label="Faint pale green tree illustration behind the contact details"></div>

    <header class="identity">
      <h1 class="identity-name">Martin Hargreave</h1>
      <p class="identity-role">owner/director</p>
    </header>

    <ul class="contact-list">
      <li class="contact-item">077 0094 5318</li>
      <li class="contact-item">020 7946 0581</li>
      <li class="contact-item">martin@hvholdings.co.uk</li>
      <li class="contact-item">hargreavehomeholdings.co.uk</li>
    </ul>

    <svg class="ground-band" viewBox="0 0 1000 130" preserveAspectRatio="none" aria-hidden="true">
      <polygon fill="var(--green)"
        points="0,22 58,4 118,30 233,4 322,30 412,4 502,30 590,4 680,30 765,4 860,30 1000,10 1000,130 0,130"/>
    </svg>
    <span class="brand-name">HARGREAVE</span>
  </article>
</body>
</html>
```